Creative Real Estate Listing Mailer

I would like a creative double sided Real Estate listing flier/mailer to send out enticing people to list their house for sale with me. An example in my head, but feel free to be creative,.. would be one side with a Weiner dog with a sack of money on its back saying something like " its time to cash in" and the other side having some kind of southwest backdrop ( I live in Arizona) or luxury home, with my photo and my contact info saying something like list your house with me, or see what your home is worth etc.

Target Market(s)

People interested in selling their homes

Industry/Entity Type

Real Estate Agent

Contact Information for Business Card

Similar to the flyer, but simpler

Requirements
Must have
• My name: Brent Holloway
My Email: brentholloway@mailvista.net
My Phone# (480) 317 4926
Website www.Brentholloway.com

```html
<!DOCTYPE html>
<html lang="en">
<head>
<meta charset="utf-8">
<title>Mesa Ridge Properties – Listing Mailer</title>
<link rel="stylesheet" href="https://fonts.googleapis.com/css2?family=Montserrat:wght@400;500;600;700;800;900&family=Kaushan+Script&display=swap">
<style>
  :root{
    --page:#e6e6e6;
    --white:#ffffff;
    --blue:#3355a0;
    --orange:#e08a1e;
    --orange-deep:#c8761a;
    --maroon:#7a1020;
    --navy:#1d2340;
    --ink:#222222;
    --stamp:#f2f2f2;
  }
  *{box-sizing:border-box;margin:0;padding:0}
  html,body{width:1200px;height:2594px;overflow:hidden;background:var(--page);font-family:"Montserrat",sans-serif;color:var(--ink)}
  .card{position:absolute;left:145px;width:900px;height:597px;background:var(--white);box-shadow:0 3px 8px rgba(0,0,0,.25);overflow:hidden}
  .card--front{top:672px}
  .card--back{top:1324px}
  .card svg.art{position:absolute;inset:0;width:900px;height:597px}

  .brand{position:absolute;display:flex;align-items:center;gap:12px;color:var(--navy);font-weight:700;letter-spacing:.06em;text-transform:uppercase;line-height:1.05}
  .brand__mark{flex:none;width:50px;height:50px;background:var(--orange)}
  .brand__name{display:flex;flex-direction:column}
  .brand--front{left:38px;top:56px;font-size:24px}
  .brand--back{left:541px;top:72px;font-size:13px;gap:8px}
  .brand--back .brand__mark{width:30px;height:30px}

  .headline{position:absolute;left:42px;top:178px;color:var(--white);line-height:1}
  .headline__lead{font-size:47px;font-weight:800;letter-spacing:.02em}
  .headline__big{display:block;margin-top:8px;margin-left:-4px;font-size:86px;font-weight:900;color:var(--orange);text-shadow:3px 3px 0 var(--orange-deep)}
  .intro{position:absolute;left:38px;top:345px;width:420px;font-size:13.5px;line-height:1.22;text-align:justify}

  .agent{position:absolute;left:62px;top:436px;color:var(--white)}
  .agent__label{font-size:22px;font-weight:400}
  .agent__name{font-family:"Kaushan Script",cursive;font-size:27px;color:var(--maroon);line-height:1.1;white-space:nowrap}
  .agent-contact{position:absolute;left:268px;top:444px;color:var(--white)}
  .agent-contact__phone{display:flex;align-items:center;gap:6px;font-size:20px;font-weight:700}
  .agent-contact__mail{display:flex;align-items:center;gap:6px;font-size:13.5px;margin-top:10px;white-space:nowrap}

  .website{position:absolute;left:38px;top:538px;width:482px;display:flex;align-items:center;gap:10px;font-size:21px;font-weight:700;color:var(--ink);white-space:nowrap}
  .website::after{content:"";flex:1;border-top:3px solid var(--ink);margin-top:4px}

  .band-title{position:absolute;left:70px;top:157px;font-size:29px;font-weight:700;color:var(--white);letter-spacing:.03em}
  .about{position:absolute;left:25px;top:232px;width:424px;color:var(--white)}
  .about h2{font-size:21px;font-weight:700;margin-bottom:12px}
  .about p{font-size:13.3px;line-height:1.25;text-align:justify}
  .back-contact{position:absolute;left:25px;top:508px;color:var(--white)}
  .back-contact__phone{display:flex;align-items:center;gap:6px;font-size:20px;font-weight:700}
  .back-contact__mail{display:flex;align-items:center;gap:6px;font-size:14px;margin-top:8px;white-space:nowrap}
  .back-web{position:absolute;left:260px;top:510px;color:var(--white);font-size:14px;display:flex;align-items:center;gap:5px;white-space:nowrap}
  .social{position:absolute;left:318px;top:540px;display:flex;gap:10px}
  .social span{width:22px;height:22px;border-radius:50%;background:var(--white)}
  .stamp{position:absolute;left:750px;top:36px;width:108px;height:108px;background:var(--stamp)}
</style>
</head>
<body>

<section class="card card--front" aria-label="Mailer front">
  <svg class="art" viewBox="0 0 900 597" aria-hidden="true">
    <path d="M0 147 Q220 150 435 160 L505 328 L0 330 Z" fill="var(--blue)"/>
    <rect x="40" y="432" width="480" height="88" rx="12" fill="var(--orange)"/>
    <path d="M372 0 L398 0 Q408 80 430 160 L410 160 Q390 80 372 0 Z" fill="var(--orange)"/>
    <g role="img" aria-label="Photo of the agent in a suit standing before a modern luxury home with a pool">
      <path d="M398 0 L900 0 L900 597 L485 597 Q488 420 505 330 L430 160 Q408 80 398 0 Z" fill="url(#frontPhoto)"/>
    </g>
    <path d="M760 510 Q850 480 900 430 L900 448 Q850 495 770 518 Z" fill="var(--maroon)"/>
    <defs>
      <linearGradient id="frontPhoto" x1="0" y1="0" x2="0" y2="1">
        <stop offset="0" stop-color="#a9c1dc"/>
        <stop offset=".45" stop-color="#b9b6ae"/>
        <stop offset=".75" stop-color="#4d6f8e"/>
        <stop offset="1" stop-color="#1f2a44"/>
      </linearGradient>
    </defs>
  </svg>

  <div class="brand brand--front"><span class="brand__mark"></span><span class="brand__name"><span>Mesa Ridge</span><span>Properties</span></span></div>

  <h1 class="headline"><span class="headline__lead">ITS TIME TO</span><span class="headline__big">CASH IN</span></h1>

  <p class="intro">Lorem ipsum dolor sit amet, consectetur adipiscing elit. Phasellus interdum turpis eu ligula ultricies semper. Proin at urna porttitor, pretium dui elementum, mattis ipsum. Phasellus tempor</p>

  <div class="agent">
    <div class="agent__label">My name</div>
    <div class="agent__name">Brent Holloway</div>
  </div>
  <div class="agent-contact">
    <div class="agent-contact__phone">
      <svg width="16" height="16" viewBox="0 0 24 24" aria-hidden="true"><path d="M6.6 10.8a15 15 0 0 0 6.6 6.6l2.2-2.2a1 1 0 0 1 1-.25 11.4 11.4 0 0 0 3.6.6 1 1 0 0 1 1 1V20a1 1 0 0 1-1 1A17 17 0 0 1 3 4a1 1 0 0 1 1-1h3.5a1 1 0 0 1 1 1c0 1.25.2 2.45.6 3.6a1 1 0 0 1-.25 1Z" fill="currentColor"/></svg>
      (480) 317 4926
    </div>
    <div class="agent-contact__mail">
      <svg width="14" height="11" viewBox="0 0 14 11" aria-hidden="true"><rect x=".5" y=".5" width="13" height="10" fill="none" stroke="currentColor"/><path d="M.5 .5 7 6 13.5 .5" fill="none" stroke="currentColor"/></svg>
      brentholloway@mailvista.net
    </div>
  </div>

  <div class="website">www.Brentholloway.com</div>
</section>

<section class="card card--back" aria-label="Mailer back">
  <svg class="art" viewBox="0 0 900 597" aria-hidden="true">
    <path d="M0 195 L482 195 Q478 420 450 597 L0 597 Z" fill="var(--blue)"/>
    <path d="M482 0 L494 0 Q518 300 460 597 L448 597 Q500 300 482 0 Z" fill="var(--orange)"/>
    <g role="img" aria-label="Photos of glass skyscrapers against a blue sky and a luxury home with a pool">
      <path d="M0 0 L472 0 Q480 80 482 150 L0 150 Z" fill="url(#backPhoto)"/>
    </g>
    <path d="M0 150 L482 150 Q483 172 482 195 L0 195 Z" fill="var(--orange)" opacity=".9"/>
    <defs>
      <linearGradient id="backPhoto" x1="0" y1="0" x2="1" y2="1">
        <stop offset="0" stop-color="#5d8fc9"/>
        <stop offset=".45" stop-color="#9fc0df"/>
        <stop offset=".75" stop-color="#d8d2c6"/>
        <stop offset="1" stop-color="#6f9a6b"/>
      </linearGradient>
    </defs>
  </svg>

  <div class="band-title">I LIVE IN ARIZONA</div>

  <div class="about">
    <h2>ABOUT US</h2>
    <p>Lorem ipsum dolor sit amet, consectetur adipiscing elit. Phasellus interdum turpis eu ligula ultricies semper. Proin at urna porttitor, pretium dui elementum, mattis ipsum. Phasellus tempor Lorem ipsum dolor sit amet, consectetur adipiscing elit. Phasellus interdum turpis eu ligula ultricies semper. Proin at urna porttitor, pretium dui elementum, mattis ipsum. Phasellus tempor Phasellus interdum turpis eu ligula ultricies semper. Proin at urna porttitor, pretium dui elementum, mattis ipsum. Phasellus tempor Lorem ipsum dolor sit amet, consectetur adipiscing elit. Phasellus interdum turpis eu ligula ultricies semper. Proin at urna porttitor, pretium dui elementum, mattis ipsum. Phasellus tempor</p>
  </div>

  <div class="back-contact">
    <div class="back-contact__phone">
      <svg width="16" height="16" viewBox="0 0 24 24" aria-hidden="true"><path d="M6.6 10.8a15 15 0 0 0 6.6 6.6l2.2-2.2a1 1 0 0 1 1-.25 11.4 11.4 0 0 0 3.6.6 1 1 0 0 1 1 1V20a1 1 0 0 1-1 1A17 17 0 0 1 3 4a1 1 0 0 1 1-1h3.5a1 1 0 0 1 1 1c0 1.25.2 2.45.6 3.6a1 1 0 0 1-.25 1Z" fill="currentColor"/></svg>
      (480) 317 4926
    </div>
    <div class="back-contact__mail">
      <svg width="14" height="11" viewBox="0 0 14 11" aria-hidden="true"><rect x=".5" y=".5" width="13" height="10" fill="none" stroke="currentColor"/><path d="M.5 .5 7 6 13.5 .5" fill="none" stroke="currentColor"/></svg>
      brentholloway@mailvista.net
    </div>
  </div>

  <div class="back-web">
    <svg width="15" height="15" viewBox="0 0 16 16" aria-hidden="true"><circle cx="8" cy="8" r="7" fill="none" stroke="currentColor"/><ellipse cx="8" cy="8" rx="3" ry="7" fill="none" stroke="currentColor"/><path d="M1 8h14M2 4.5h12M2 11.5h12" stroke="currentColor" fill="none"/></svg>
    www.Brentholloway.com
  </div>
  <div class="social" aria-label="Social profiles"><span></span><span></span></div>

  <div class="brand brand--back"><span class="brand__mark"></span><span class="brand__name"><span>Mesa Ridge</span><span>Properties</span></span></div>
  <div class="stamp" aria-label="Postage stamp area"></div>
</section>

</body>
</html>
```